Brookfarrow Osteopathy and dry needling business card

Business card for Brookfarrow Osteopathy and Dry Needling.

Industry/Entity Type

Health

Contact Information for Business Card

I do not have a phone number yet. I also do not have an email address yet. The physical address is: 48 Lower Crane Street Brookfarrow The website is: www.brookfarrowosteosteopathy.example My details are: Dr Martin Pellowe, Osteopath (B.Clin.Sci (Ost) M.Ost BSC ECON (Hons)

Colors
0094D4
00A9DD
6FCCEA
C7EBF8
E9F6FB

Requirements
Must have
• logo on the back
Nice to have
• Maybe a space for me to write an appointment time and date on the card.

```html
<!DOCTYPE html>
<html lang="en">
<head>
<meta charset="utf-8">
<title>Brookfarrow Osteopathy and Dry Needling – Business Card</title>
<link href="https://fonts.googleapis.com/css2?family=Montserrat:wght@700&family=Open+Sans:wght@400;600&display=swap" rel="stylesheet">
<style>
  :root {
    --page-bg: #2a2b2d;
    --card-dark: #1c1d1f;
    --card-light: #e6e6e6;
    --brand-blue: #0094d4;
    --brand-orange: #f08a1e;
    --text-light: #f4f4f4;
    --text-muted: #6b6b6b;
    --rule-grey: #9a9a9a;
  }
  * { margin: 0; padding: 0; box-sizing: border-box; }
  html, body { width: 1200px; height: 1108px; overflow: hidden; }
  body {
    background: var(--page-bg);
    font-family: "Open Sans", Arial, sans-serif;
    position: relative;
  }
  .card {
    position: absolute;
    top: 214px;
    width: 420px;
    height: 680px;
    border-radius: 22px;
    background: var(--card-dark);
    overflow: hidden;
    box-shadow: 0 18px 40px rgba(0,0,0,0.45);
  }
  .card--front { left: 150px; }
  .card--back { left: 630px; }

  /* Front */
  .brand-mark {
    position: absolute;
    top: 48px; left: 50%;
    transform: translateX(-50%);
    width: 250px; height: 250px;
    border: 3px solid var(--brand-blue);
    border-radius: 50%;
    display: flex; align-items: center; justify-content: center;
    text-align: center;
  }
  .brand-name {
    color: var(--brand-blue);
    font-weight: 600;
    font-size: 22px;
    line-height: 1.3;
    letter-spacing: 0.04em;
    text-transform: uppercase;
    padding: 0 24px;
  }
  .details {
    position: absolute;
    top: 320px; left: 0; right: 0;
    text-align: center;
    color: var(--text-light);
  }
  .practitioner {
    font-family: "Montserrat", Arial, sans-serif;
    font-weight: 700;
    font-size: 23px;
    color: var(--brand-blue);
    text-transform: uppercase;
  }
  .role { font-size: 17px; margin-top: 2px; }
  .qualifications { font-size: 15px; margin-top: 2px; }
  .divider {
    width: 80px; height: 1px;
    background: var(--brand-blue);
    margin: 14px auto;
  }
  .contact-line { font-size: 15px; line-height: 1.5; }
  .contact-line .domain { color: var(--brand-orange); }
  .address { font-size: 16px; }

  .appointment {
    position: absolute;
    left: 0; right: 0; bottom: 0;
    height: 150px;
    background: var(--card-light);
    padding: 28px 30px 0;
  }
  .appointment-title {
    text-align: center;
    color: var(--brand-orange);
    font-weight: 600;
    font-size: 24px;
    letter-spacing: 0.01em;
  }
  .appointment-fields {
    display: flex;
    align-items: flex-end;
    gap: 8px;
    margin-top: 26px;
    color: var(--text-muted);
    font-size: 17px;
  }
  .field-line {
    flex: 1;
    border-bottom: 1px solid var(--rule-grey);
    height: 18px;
  }
  .field-suffix { font-size: 12px; }

  /* Back */
  .pattern-fill {
    position: absolute; inset: 0;
    background: radial-gradient(circle at 40% 40%, #232427 0%, #1b1c1e 70%);
  }
  .back-mark {
    position: absolute;
    right: 70px; bottom: 150px;
    display: flex; align-items: center; gap: 8px;
  }
  .back-mark-dot {
    width: 16px; height: 16px;
    border: 2px solid var(--brand-blue);
    border-radius: 50%;
  }
  .back-mark-name {
    color: var(--brand-blue);
    font-weight: 600;
    font-size: 13px;
    text-transform: uppercase;
    letter-spacing: 0.04em;
  }
</style>
</head>
<body>
  <section class="card card--front" aria-label="Business card front">
    <div class="brand-mark">
      <span class="brand-name">Brookfarrow Osteopathy &amp; Dry Needling</span>
    </div>

    <div class="details">
      <h1 class="practitioner">Dr Martin Pellowe</h1>
      <p class="role">Osteopath</p>
      <p class="qualifications">(B.Clin.Sci (Ost) M.Ost BSC ECON (Hons)</p>
      <div class="divider"></div>
      <p class="contact-line">info@brookfarrowosteosteopathy.example</p>
      <p class="contact-line">www.<span class="domain">brookfarrowosteosteopathy</span>.example</p>
      <div class="divider"></div>
      <p class="address">48 Lower Crane Street Brookfarrow</p>
    </div>

    <div class="appointment">
      <h2 class="appointment-title">YOUR NEXT APPOINTMENT</h2>
      <div class="appointment-fields">
        <span>Date:</span><span class="field-line"></span>
        <span>Time:</span><span class="field-line"></span>
        <span class="field-suffix">AM/PM</span>
      </div>
    </div>
  </section>

  <section class="card card--back" aria-label="Business card back">
    <div class="pattern-fill" role="img" aria-label="Tone-on-tone embossed repeating brand pattern"></div>
    <div class="back-mark">
      <span class="back-mark-dot"></span>
      <span class="back-mark-name">Brookfarrow</span>
    </div>
  </section>
</body>
</html>
```